Website Design for Harbor Guide

I am looking to create a website to help military members who are currently serving or have served to have a mentor. The military does an awful job and providing or offering a mentor program. People need someone they can come to with career advice with promotions, networking, building resumes, and pinging ideas off of on the occasion. I want a place where active and separated military members can come to, sign up and pick a program of offerings that make sense. They would register annually, pay for a membership package (can choose up to three) and then get support they need. Annual registration fees would be as follows and they would need to send payment through Paywisp or other electronic means (credit card, eft, paywisp, echeck, whatever).

I envision some type of registration that centers around the packages offered - this will be where the revision comes in once the framework is completed.

I am looking for very creative designs, and content, given the above, with verbiage around mentorship program. Please be creative for the design, and also put together three packages and price points for them three packages - put together what it would include in each package. We can modify as necessary during revisions. Final design should communicate military members in uniform with corporate leaders, something warm and inviting are important. I also want the abiity to really get this adversited and in the market for people to stumble across it easily.

I have purchased the domain already - harborguide.com

Target Market(s)

Military, Veterans

Number of Pages Required

1 page

Requirements
Must have
• Military member with corporate look
• Modern and wide
• Warm and inviting
• Registration with ability to collect through PayWisp, eCheck, Credit Card, etc)
• Creative design and content for the website based on what is described in the description
• About Section which has information about leadership team
• Contact Us
• Register
• 3 creative packages of what would be included (design this and the content keeping in mind the description)
• Content and the framework
• Some type of packages to consider (just examples but also needs mentoring options:
• https://www.careerpenworks.com/
• https://www.vitaecrest.com/
• We are not going to ba resume writing service but we will offer it as part of our solution - I really want it to be focused around mentorship for job development, professional advice, interacting with peers, managers, leaders (using military acronyms like Supervisors and Leaders NCO's, Officers, etc)
• Blog so we can post topics and interact and respond to questions people have etc

```html
<!DOCTYPE html>
<html lang="en">
<head>
<meta charset="utf-8">
<title>Harbor Guide — Mentorship for Service Members</title>
<link href="https://fonts.googleapis.com/css2?family=Montserrat:wght@400;500;600;700;800&display=swap" rel="stylesheet">
<style>
:root{
  --navy:#1f2759;
  --navy-deep:#17204c;
  --red:#e0213f;
  --ink:#1d1d1d;
  --text:#555a66;
  --card:#f2f2f2;
  --teal:#4fcbb2;
  --blue:#3b8fd5;
  --pink:#e8566c;
  --footer:#2b2b2d;
  --footer-bar:#1c1c1e;
  --white:#ffffff;
}
*{box-sizing:border-box;margin:0;padding:0}
html,body{width:1200px;height:3896px;overflow:hidden}
body{font-family:"Montserrat",Arial,sans-serif;color:var(--text);background:var(--white);position:relative}
.wrap{width:1054px;margin:0 auto;position:relative;height:100%}
.btn{display:inline-block;font-family:inherit;font-weight:500;border:none;border-radius:3px;color:var(--white);background:var(--red);text-align:center}

/* header */
.site-header{height:86px;position:relative}
.logo{position:absolute;left:0;top:30px;font-size:30px;font-weight:700;color:var(--navy);letter-spacing:-.5px}
.callout{position:absolute;right:0;top:6px;font-size:13px;color:var(--ink)}
.callout b{color:var(--navy);font-weight:700}
.main-nav{position:absolute;right:0;top:38px;display:flex;align-items:center;gap:30px;font-size:14px;font-weight:500;color:var(--ink);text-transform:uppercase}
.main-nav .btn{font-size:13px;padding:7px 12px;text-transform:none}
.main-nav .btn-login{background:var(--navy);padding:7px 24px}
.main-nav .btn + .btn{margin-left:-20px}

/* hero */
.hero{height:545px;position:relative;overflow:hidden;
  background:linear-gradient(100deg,#e9e6e8 0%,#f3d9dc 22%,#e9b2ba 42%,#c9b39a 62%,#8c8466 78%,#5e5b4a 100%)}
.hero-photo{position:absolute;inset:0}
.hero-panel{position:absolute;left:73px;top:70px;width:571px;height:376px;background:rgba(255,255,255,.92);padding:52px 28px 0 28px}
.hero-panel::before,.hero-panel::after{content:"";position:absolute;left:-6px;width:46px;height:46px;border-left:8px solid var(--navy)}
.hero-panel::before{top:-6px;border-top:8px solid var(--navy)}
.hero-panel::after{bottom:-6px;border-bottom:8px solid var(--navy)}
.hero-panel h1{font-size:42px;font-weight:700;color:var(--ink);line-height:1.1;margin-bottom:18px}
.hero-panel p{font-size:16px;line-height:1.6;color:#333;margin-bottom:28px}
.hero-panel .btn{font-size:22px;padding:12px 24px}

/* about */
.about{height:340px;background:var(--navy);color:var(--white);text-align:center;padding-top:50px}
.section-title{display:flex;align-items:center;justify-content:center;gap:24px;font-size:31px;font-weight:600;margin-bottom:26px}
.section-title::before,.section-title::after{content:"";width:165px;height:1px;background:rgba(255,255,255,.35)}
.about p{font-size:14px;line-height:1.7;width:1054px;margin:0 auto 26px}
.btn-outline{background:transparent;border:1.5px solid var(--white);font-size:14px;padding:10px 22px}

/* features */
.features{height:514px;padding-top:52px}
.features .wrap{display:flex;gap:27px}
.feature-card{flex:1;height:413px;background:var(--card);border-radius:4px;box-shadow:0 2px 6px rgba(0,0,0,.12);text-align:center;padding:30px 26px 0}
.feature-card svg{display:block;margin:0 auto 30px}
.feature-card h3{font-size:19px;font-weight:700;color:var(--ink);margin-bottom:22px}
.feature-card p{font-size:14px;line-height:1.75}

/* join */
.join{height:354px;background:radial-gradient(ellipse at center,#e6e6e6 0%,#cfcfcf 60%,#b9b9b9 100%);position:relative;padding-top:29px}
.join-box{width:893px;height:304px;margin:0 auto;background:rgba(255,255,255,.9);text-align:center;padding-top:34px}
.ribbon{display:inline-flex;align-items:center;margin-bottom:24px}
.ribbon span{background:var(--navy);color:var(--white);font-size:29px;font-weight:700;padding:8px 36px}
.join-box p{font-size:15px;line-height:1.7;width:800px;margin:0 auto 22px;color:#444}
.join-box .btn{font-size:22px;padding:11px 38px}

/* packages */
.packages{height:748px;background:radial-gradient(ellipse at 50% 40%,#2a3470 0%,var(--navy) 55%,var(--navy-deep) 100%);color:var(--white);padding-top:46px;text-align:center}
.packages .section-title{margin-bottom:28px}
.packages .section-title::before,.packages .section-title::after{width:0}
.plan-row{display:flex;justify-content:center;gap:26px;margin-bottom:22px}
.plan{width:298px;height:494px;background:var(--white);border-radius:6px;overflow:hidden;color:var(--text);text-align:left}
.plan-head{padding:12px 0 0;text-align:center;font-size:29px;font-weight:700;color:var(--white)}
.plan-price{display:flex;align-items:center;justify-content:center;gap:10px;padding:10px 0 14px;color:var(--white)}
.plan-price .amount{font-size:64px;font-weight:700;line-height:1}
.plan-price .amount sup{font-size:26px;vertical-align:top;position:relative;top:6px}
.plan-price .label{font-size:14px;line-height:1.2;text-align:left}
.plan.teal .top{background:var(--teal)} .plan.teal .plan-price{background:#43b7a0}
.plan.blue .top{background:var(--blue)} .plan.blue .plan-price{background:#327ec0}
.plan.pink .top{background:var(--pink)} .plan.pink .plan-price{background:#d84a60}
.plan ul{list-style:none;padding:8px 20px 0}
.plan li{font-size:14px;padding:11px 0;border-bottom:1px solid #e3e3e3;color:#444}
.plan .btn{display:block;margin:22px auto 0;width:156px;font-size:20px;padding:8px 0}
.pay-note{font-size:14px}
.pay-note strong{display:block;font-size:19px;font-weight:500;margin-top:6px}

/* testimonials */
.testimonials{height:452px;background:linear-gradient(180deg,#eeeeee,#e3e3e3);padding-top:48px}
.testimonials h2{font-size:32px;font-weight:700;color:var(--ink)}
.arrows{position:absolute;right:0;top:2px;display:flex;gap:14px}
.quote-row{display:flex;gap:34px;margin-top:30px}
.quote{flex:1;height:221px;background:var(--white);border-radius:4px;box-shadow:0 1px 4px rgba(0,0,0,.12);padding:20px 24px;position:relative}
.quote p{font-size:15px;line-height:1.6;color:#444;width:410px}
.quote .name{margin-top:16px;font-size:16px;font-weight:700;color:var(--ink)}
.quote .role{font-size:13px}
.avatar{position:absolute;right:18px;bottom:-32px;width:112px;height:112px;border-radius:50%;border:4px solid var(--white);background:radial-gradient(circle at 50% 40%,#b98a6c 0%,#7b5a47 60%,#3c2e27 100%);box-shadow:0 1px 4px rgba(0,0,0,.25)}

/* blog + contact */
.blog{height:576px;padding-top:60px}
.blog h2{font-size:32px;font-weight:700;color:var(--ink);margin-bottom:20px}
.posts{display:flex;gap:26px;width:671px}
.post{width:335px}
.post-media{height:187px;position:relative;background:linear-gradient(120deg,#b9b39d,#6f6b55 55%,#2e2d27)}
.post-media.alt{background:linear-gradient(120deg,#8d8a7d,#4f4c42 50%,#17171a)}
.date-tag{position:absolute;right:0;top:0;width:56px;height:187px;background:rgba(31,39,89,.92);color:var(--white);text-align:center;padding-top:10px;font-size:11px;line-height:1.1}
.date-tag .day{font-size:24px;font-weight:700;display:block;margin:2px 0}
.date-tag .count{position:absolute;bottom:12px;left:0;right:0}
.post h3{font-size:16px;font-weight:700;color:var(--ink);margin-top:14px}
.post .by{font-size:12px;margin:4px 0 8px}
.post p{font-size:13px;line-height:1.6}
.read-more{display:inline-block;margin-top:12px;font-size:13px;font-weight:700;color:var(--red)}
.quick-contact{position:absolute;right:0;top:-3px;width:332px;height:425px;background:var(--navy);padding:18px 18px}
.quick-contact h3{font-size:29px;font-weight:600;color:var(--white);margin-bottom:16px}
.field{background:var(--white);height:46px;margin-bottom:12px;font-size:13px;color:#666;padding:13px 12px}
.field.area{height:92px}
.quick-contact .btn{display:block;width:100%;height:44px;font-size:22px;font-weight:700;margin-top:2px}

/* footer */
.site-footer{height:234px;background:var(--footer);color:#dcdcdc;padding-top:42px}
.site-footer .wrap{display:flex}
.f-col h4{font-size:13px;font-weight:700;color:var(--white);margin-bottom:18px;text-transform:uppercase}
.f-col ul{list-style:none;font-size:13px;line-height:1.9}
.f-col p{font-size:13px}
.f-news{margin-left:115px;width:294px}
.f-news .email-box{background:var(--white);height:38px;margin:10px 0 10px;color:#777;font-size:12px;padding:11px 12px}
.f-news .btn{display:block;width:100%;height:34px;font-size:14px;font-weight:700;padding-top:9px}
.f-social{margin-left:44px;width:250px}
.socials{display:flex;gap:6px;margin-bottom:14px}
.socials span{width:38px;height:38px;border-radius:50%;border:2px solid #e6e6e6}
.cards{display:flex;gap:6px}
.cards span{width:42px;height:26px;background:var(--white);border-radius:2px;color:var(--navy);font-size:9px;font-weight:600;display:flex;align-items:center;justify-content:center}
.f-contact{margin-left:18px}
.f-contact .big{font-size:25px;font-weight:700;color:var(--white);margin:4px 0 14px}
.f-contact .mail{font-size:15px;font-weight:700;color:var(--white);margin-top:4px}
.footer-bar{height:47px;background:var(--footer-bar);color:#e0e0e0;font-size:13px}
.footer-bar .wrap{display:flex;justify-content:space-between;align-items:center}
.footer-bar nav{display:flex;gap:28px}
</style>
</head>
<body>

<header class="site-header">
  <div class="wrap">
    <div class="logo">Harbor Guide</div>
    <div class="callout">Let's help you now! Call <b>(800) 555-0147</b></div>
    <nav class="main-nav">
      <span>Home</span><span>About Us</span><span>How It Works</span><span>Contact Us</span>
      <span class="btn">Start Now!</span><span class="btn btn-login">Log In</span>
    </nav>
  </div>
</header>

<section class="hero">
  <div class="hero-photo" role="img" aria-label="Uniformed service member in camouflage and patrol cap looking upward before a waving striped flag"></div>
  <div class="hero-panel">
    <h1>Build Your Networking</h1>
    <p>Lorem ipsum dolor sit amet, consectetur adipiscing elit, sed do eiusmod tempor incididunt ut labore et dolore magna aliqua. Ut enim ad minim veniam, quis nostrud exercitation ullamco laboris nisi ut aliquip ex ea commodo consequat.</p>
    <span class="btn">Start Now!</span>
  </div>
</section>

<section class="about">
  <h2 class="section-title">About Harbor Guide</h2>
  <p>Lorem ipsum dolor sit amet, consectetur adipiscing elit, sed do eiusmod tempor incididunt ut labore et dolore magna aliqua. Ut enim ad minim veniam, quis nostrud exercitation ullamco laboris nisi ut aliquip ex ea commodo consequat. Duis aute irure dolor in reprehenderit in voluptate velit esse cillum dolore eu fugiat nulla pariatur. Excepteur sint occaecat cupidatat non proident, sunt in culpa qui officia deserunt mollit anim id est laborum.</p>
  <span class="btn btn-outline">Read More</span>
</section>

<section class="features">
  <div class="wrap">
    <article class="feature-card">
      <svg width="90" height="90" viewBox="0 0 90 90"><circle cx="45" cy="45" r="43" fill="#1c86d8"/><circle cx="45" cy="45" r="37" fill="none" stroke="#fff" stroke-opacity=".35" stroke-width="1.5"/><text x="45" y="59" text-anchor="middle" font-family="Montserrat,Arial,sans-serif" font-size="42" font-weight="700" fill="#fff">?</text></svg>
      <h3>What is Harbor Guide?</h3>
      <p>Sed ut perspiciatis unde omnis iste natus error sit voluptatem accusantium doloremque laudantium, totam rem aperiam, eaque ipsa quae ab illo inventore veritatis et quasi architecto beatae vitae dicta sunt explicabo.</p>
    </article>
    <article class="feature-card">
      <svg width="90" height="90" viewBox="0 0 90 90"><circle cx="45" cy="45" r="43" fill="#e0661b"/><circle cx="45" cy="45" r="37" fill="none" stroke="#fff" stroke-opacity=".35" stroke-width="1.5"/><text x="45" y="59" text-anchor="middle" font-family="Montserrat,Arial,sans-serif" font-size="38" font-weight="700" fill="#fff">$</text></svg>
      <h3>The Program</h3>
      <p>Sed ut perspiciatis unde omnis iste natus error sit voluptatem accusantium doloremque laudantium, totam rem aperiam, eaque ipsa quae ab illo inventore veritatis et quasi architecto beatae vitae dicta sunt explicabo.</p>
    </article>
    <article class="feature-card">
      <svg width="90" height="90" viewBox="0 0 90 90"><circle cx="45" cy="45" r="43" fill="#4fae1f"/><circle cx="45" cy="45" r="37" fill="none" stroke="#fff" stroke-opacity=".35" stroke-width="1.5"/><rect x="29" y="29" width="32" height="32" fill="none" stroke="#fff" stroke-width="3"/><rect x="34" y="47" width="4" height="10" fill="#fff"/><rect x="41" y="42" width="4" height="15" fill="#fff"/><rect x="48" y="38" width="4" height="19" fill="#fff"/><path d="M33 42 L42 35 L48 38 L57 31" stroke="#fff" stroke-width="2.5" fill="none"/></svg>
      <h3>Mentoring = Results</h3>
      <p>Sed ut perspiciatis unde omnis iste natus error sit voluptatem accusantium doloremque laudantium, totam rem aperiam, eaque ipsa quae ab illo inventore veritatis et quasi architecto beatae vitae dicta sunt explicabo.</p>
    </article>
  </div>
</section>

<section class="join">
  <div class="join-box">
    <div class="ribbon">
      <svg width="44" height="30" viewBox="0 0 44 30"><path d="M0 0 H44 V30 H0 L10 15 Z" fill="#1f2759"/><path d="M30 0 L30 30" stroke="#fff" stroke-width="2"/></svg>
      <span>Join Us Today</span>
      <svg width="44" height="30" viewBox="0 0 44 30"><path d="M0 0 H44 L34 15 L44 30 H0 Z" fill="#1f2759"/><path d="M14 0 L14 30" stroke="#fff" stroke-width="2"/></svg>
    </div>
    <p>Lorem ipsum dolor sit amet, consectetur adipiscing elit, sed do eiusmod tempor incididunt ut labore et dolore magna aliqua. Ut enim ad minim veniam, quis nostrud exercitation ullamco laboris nisi ut aliquip ex ea commodo consequat.</p>
    <span class="btn">Register Now!</span>
  </div>
</section>

<section class="packages">
  <h2 class="section-title">Membership Package</h2>
  <div class="plan-row">
    <article class="plan teal">
      <div class="top"><div class="plan-head">Program 01</div></div>
      <div class="plan-price"><span class="amount"><sup>$</sup>90</span><span class="label">Annual<br>Registration Fees</span></div>
      <ul><li>Lorem ipsum dolor sit amet.</li><li>Duis aute irure dolor.</li><li>Sed ut perspiciatis unde omnis iste</li><li>Ut enim ad minima veniam.</li><li>Neque porro quisquam est</li><li>Lorem ipsum dolor sit amet.</li></ul>
      <span class="btn">Sign Up</span>
    </article>
    <article class="plan blue">
      <div class="top"><div class="plan-head">Program 02</div></div>
      <div class="plan-price"><span class="amount"><sup>$</sup>130</span><span class="label">Annual<br>Registration Fees</span></div>
      <ul><li>Lorem ipsum dolor sit amet.</li><li>Duis aute irure dolor.</li><li>Sed ut perspiciatis unde omnis iste</li><li>Ut enim ad minima veniam.</li><li>Neque porro quisquam est</li><li>Lorem ipsum dolor sit amet.</li></ul>
      <span class="btn">Sign Up</span>
    </article>
    <article class="plan pink">
      <div class="top"><div class="plan-head">Program 03</div></div>
      <div class="plan-price"><span class="amount"><sup>$</sup>140</span><span class="label">Annual<br>Registration Fees</span></div>
      <ul><li>Lorem ipsum dolor sit amet.</li><li>Duis aute irure dolor.</li><li>Sed ut perspiciatis unde omnis iste</li><li>Ut enim ad minima veniam.</li><li>Neque porro quisquam est</li><li>Lorem ipsum dolor sit amet.</li></ul>
      <span class="btn">Sign Up</span>
    </article>
  </div>
  <p class="pay-note">Follows and they would need to send payment through<strong>Paywisp or other electronic means (credit card, eft, paywisp, echeck, whatever)</strong></p>
</section>

<section class="testimonials">
  <div class="wrap">
    <h2>Testimonials</h2>
    <div class="arrows">
      <svg width="26" height="26" viewBox="0 0 26 26"><circle cx="13" cy="13" r="12" fill="#d0d0d0"/><path d="M15 8 L10 13 L15 18" stroke="#fff" stroke-width="2.5" fill="none"/></svg>
      <svg width="26" height="26" viewBox="0 0 26 26"><circle cx="13" cy="13" r="11" fill="none" stroke="#1d1d1d" stroke-width="2"/><path d="M11 8 L16 13 L11 18" stroke="#1d1d1d" stroke-width="2.5" fill="none"/></svg>
    </div>
    <div class="quote-row">
      <article class="quote">
        <p>"Lorem ipsum dolor sit amet, consectetur adipiscing elit, sed do eiusmod tempor incididunt ut labore et dolore magna aliqua. Ut enim ad minim veniam, quis nostrud exercitation ullamco laboris nisi ut aliquip ex ea commodo consequat. esse cillum dolore eu fugiat nulla pariatur."</p>
        <div class="name">Dale Rourke</div><div class="role">Lorem ipsum dolor</div>
        <div class="avatar" role="img" aria-label="Portrait photo of the member giving this testimonial"></div>
      </article>
      <article class="quote">
        <p>"Lorem ipsum dolor sit amet, consectetur adipiscing elit, sed do eiusmod tempor incididunt ut labore et dolore magna aliqua. Ut enim ad minim veniam, quis nostrud exercitation ullamco laboris nisi ut aliquip ex ea commodo consequat. esse cillum dolore eu fugiat nulla pariatur."</p>
        <div class="name">Marcus Hale</div><div class="role">Lorem ipsum dolor</div>
        <div class="avatar" role="img" aria-label="Portrait photo of the member giving this testimonial"></div>
      </article>
    </div>
  </div>
</section>

<section class="blog">
  <div class="wrap">
    <h2>Latest Blog</h2>
    <div class="posts">
      <article class="post">
        <div class="post-media" role="img" aria-label="Service member in field gear and camouflage">
          <div class="date-tag">FEB<span class="day">08</span>2018<span class="count">22</span></div>
        </div>
        <h3>Lorem ipsum dolor sit amet, consec.</h3>
        <div class="by">By Marcus Hale</div>
        <p>Sed ut perspiciatis unde omnis iste natus error sit voluptatem accusantium doloremque laudantium, totam rem aperiam, eaque ipsa quae ab illo inventore.</p>
        <span class="read-more">Read More ▸</span>
      </article>
      <article class="post">
        <div class="post-media alt" role="img" aria-label="Service member wearing a helmet and headset">
          <div class="date-tag">FEB<span class="day">08</span>2018<span class="count">22</span></div>
        </div>
        <h3>Lorem ipsum dolor sit amet, consec.</h3>
        <div class="by">By Marcus Hale</div>
        <p>Sed ut perspiciatis unde omnis iste natus error sit voluptatem accusantium doloremque laudantium, totam rem aperiam, eaque ipsa quae ab illo inventore.</p>
        <span class="read-more">Read More ▸</span>
      </article>
    </div>
    <aside class="quick-contact">
      <h3>Quick Contact</h3>
      <div class="field">Name</div>
      <div class="field">Email</div>
      <div class="field">Phone</div>
      <div class="field area">Message</div>
      <span class="btn">Submit</span>
    </aside>
  </div>
</section>

<footer class="site-footer">
  <div class="wrap">
    <div class="f-col">
      <h4>Quick Links</h4>
      <ul><li>Home</li><li>About Us</li><li>How It Works</li><li>Contact Us</li></ul>
    </div>
    <div class="f-col f-news">
      <h4>Subscribe Newsletter</h4>
      <p>Join our email list for news</p>
      <div class="email-box">Your Email</div>
      <span class="btn">SIGN UP</span>
    </div>
    <div class="f-col f-social">
      <h4>Get Connect With Us</h4>
      <div class="socials">
        <span role="img" aria-label="Chatterly"></span><span role="img" aria-label="Chirpnet"></span><span role="img" aria-label="Linkfolio"></span><span role="img" aria-label="Pinboardly"></span>
      </div>
      <h4 style="margin-bottom:10px">We Accept</h4>
      <div class="cards"><span>Vexa</span><span>PayWisp</span><span>Mintcard</span><span>Amberline</span><span>Discovo</span></div>
    </div>
    <div class="f-col f-contact">
      <h4>Contact Us</h4>
      <p>Phone</p>
      <div class="big">(800) 555-0147</div>
      <p>Email</p>
      <div class="mail">info@harborguide.com</div>
    </div>
  </div>
</footer>
<div class="footer-bar">
  <div class="wrap">
    <span>Harbor Guide © 2018 - All Rights Reserved</span>
    <nav><span>Terms of Use</span><span>Privacy Policy</span></nav>
  </div>
</div>

</body>
</html>
```